Life and Personal development life coach needs card design

I need a card design that matches the style and design of my website. I'd like to stay in the same color scheme. Please check out my website for ideas. www.brivelmorcott.com
I have had previous designs for this. I am wondering if you have access to those for more ideas??

```html
<!DOCTYPE html>
<html lang="en">
<head>
<meta charset="utf-8">
<title>Brivel Morcott — Business Card</title>
<link rel="stylesheet" href="https://fonts.googleapis.com/css2?family=Jura:wght@500;600&family=Roboto+Slab:wght@700&family=Open+Sans:wght@400&display=swap">
<style>
  :root {
    --bg: #1b1b1b;
    --lime: #9cca1a;
    --lime-light: #bfe04e;
    --lime-pale: #e6f3b8;
    --olive: #6f9a12;
    --white: #ffffff;
    --ink: #2b2b2b;
    --grey: #3a3a3a;
  }
  * { margin: 0; padding: 0; box-sizing: border-box; }
  html, body { width: 1200px; height: 974px; overflow: hidden; background: var(--bg); }
  .stage { position: relative; width: 1200px; height: 974px; }

  .card {
    position: absolute;
    width: 340px;
    height: 595px;
    overflow: hidden;
    box-shadow: 0 12px 30px rgba(0,0,0,.55);
  }
  .card--front { left: 220px; top: 190px; background: var(--white); }
  .card--back {
    left: 640px; top: 190px;
    background: radial-gradient(ellipse at 55% 45%, var(--white) 0%, var(--white) 22%, var(--lime-pale) 55%, var(--lime-light) 85%, var(--lime) 100%);
  }

  .card__edges { position: absolute; inset: 0; }

  .brand {
    position: absolute;
    left: 50px; top: 140px; width: 250px;
    text-align: center;
  }
  .brand__mark {
    display: block;
    width: 30px; height: 30px;
    margin: 0 auto 12px;
    background: var(--lime);
  }
  .brand__name {
    font-family: "Jura", sans-serif;
    font-weight: 600;
    font-size: 28px;
    color: var(--lime);
    letter-spacing: .5px;
    line-height: 1;
  }
  .brand__tagline {
    font-family: "Roboto Slab", serif;
    font-weight: 700;
    font-size: 10px;
    color: var(--ink);
    margin-top: 6px;
    white-space: nowrap;
  }

  .contact { position: absolute; left: 118px; top: 395px; width: 200px; }
  .contact__rule { height: 2px; background: var(--lime); margin-bottom: 8px; }
  .contact__row {
    display: flex; align-items: center; gap: 8px;
    height: 36px;
    border-bottom: 2px solid var(--lime);
    margin-bottom: 6px;
  }
  .contact__icon {
    width: 32px; height: 32px; flex: none;
    background: var(--lime);
    display: flex; align-items: center; justify-content: center;
  }
  .contact__text {
    font-family: "Open Sans", sans-serif;
    font-size: 12.5px;
    color: var(--ink);
    white-space: nowrap;
  }
  .contact__text--phone { font-size: 16px; }

  .back-mark {
    position: absolute;
    left: 120px; top: 150px;
    width: 26px; height: 26px;
    background: var(--lime);
  }
  .back-name {
    position: absolute;
    left: 200px; top: 90px;
    transform-origin: left top;
    transform: rotate(90deg);
    font-family: "Jura", sans-serif;
    font-weight: 500;
    font-size: 38px;
    color: var(--grey);
    white-space: nowrap;
    letter-spacing: 1px;
  }
</style>
</head>
<body>
<main class="stage">

  <section class="card card--front" aria-label="Card front">
    <svg class="card__edges" viewBox="0 0 340 595" aria-hidden="true">
      <path d="M0 0 H22 C44 150 44 330 0 450 Z" fill="var(--lime)"/>
      <path d="M0 0 H10 C26 140 24 320 0 410 Z" fill="var(--olive)" opacity=".35"/>
      <path d="M0 0 H340 V10 C250 2 130 2 0 20 Z" fill="var(--lime-light)"/>
      <path d="M340 0 V230 C322 170 312 60 300 0 Z" fill="var(--lime)"/>
      <path d="M340 0 V130 C328 100 320 40 314 0 Z" fill="var(--olive)" opacity=".3"/>
      <path d="M340 595 V455 C326 520 300 570 240 595 Z" fill="var(--lime)"/>
      <path d="M340 595 V515 C330 555 312 580 285 595 Z" fill="var(--olive)" opacity=".3"/>
      <path d="M0 595 V530 C30 560 65 582 105 595 Z" fill="var(--lime-light)"/>
    </svg>

    <div class="brand">
      <span class="brand__mark" aria-hidden="true"></span>
      <p class="brand__name">Brivel Morcott</p>
      <p class="brand__tagline">life and personal development life coach</p>
    </div>

    <div class="contact">
      <div class="contact__rule"></div>
      <div class="contact__row">
        <span class="contact__icon">
          <svg width="20" height="20" viewBox="0 0 20 20" aria-hidden="true">
            <path d="M3 7 C3 4 17 4 17 7 L15 9 L13 7 H7 L5 9 Z" fill="#fff"/>
            <rect x="5" y="10" width="10" height="7" rx="1" fill="#fff"/>
          </svg>
        </span>
        <span class="contact__text contact__text--phone">555-014-2286</span>
      </div>
      <div class="contact__row">
        <span class="contact__icon">
          <svg width="22" height="16" viewBox="0 0 22 16" aria-hidden="true">
            <rect x="1" y="1" width="20" height="14" fill="none" stroke="#fff" stroke-width="1.6"/>
            <path d="M1 1 L11 9 L21 1" fill="none" stroke="#fff" stroke-width="1.6"/>
          </svg>
        </span>
        <span class="contact__text">www.brivelmorcott.com</span>
      </div>
      <div class="contact__row">
        <span class="contact__icon">
          <svg width="20" height="20" viewBox="0 0 20 20" aria-hidden="true">
            <circle cx="10" cy="10" r="8" fill="none" stroke="#fff" stroke-width="1.5"/>
            <ellipse cx="10" cy="10" rx="3.5" ry="8" fill="none" stroke="#fff" stroke-width="1.2"/>
            <path d="M2 10 H18 M3.5 6 H16.5 M3.5 14 H16.5" stroke="#fff" stroke-width="1.2"/>
          </svg>
        </span>
        <span class="contact__text">brivel@brivelmorcott.com</span>
      </div>
    </div>
  </section>

  <section class="card card--back" aria-label="Card back">
    <span class="back-mark" aria-hidden="true"></span>
    <p class="back-name">Brivel Morcott</p>
  </section>

</main>
</body>
</html>
```